Claimant Aid Pathway USA - Email Marketing Creative

Looking for design of email creative for Claimant Aid Pathway USA website. Call to action based email focused on conveying brand, messaging of "Disabled? Unable to Work? You May Qualify for Social Security Disability Benefits", call to action of 'Free Evaluation' or 'Fast, Free, No Obligation Evaluation'. Can use any messaging from the current mock of https://lnkshrt.example/7QwXpR4 . Please focus on imaging of 50+ people if used, red white and blue coloring (patriotic) yet USA looking. Creative must be done in HTML as well as text for easy use and include Email Opt Out link etc. Examples of competitors emails attached. PLEASE DO NOT COPY them. Just use as examples.

Target Market(s)

Disabled American. Age 50+ Looking for help applying, re-applying or handling a social security disability hearing.

Industry/Entity Type

Legal

Font styles to use
Serif
Sans Serif

Colors

Designer to choose colors to be used in the design.

Requirements
Must have
• call to action based html
Nice to have
• strong call to action.
Should not have
• Should not be cookie cutter. Stick to simple yet official looking.

```html
<!DOCTYPE html>
<html lang="en">
<head>
<meta charset="utf-8">
<title>Claimant Aid Pathway USA – Email</title>
<link href="https://fonts.googleapis.com/css2?family=Poppins:wght@400;500;600;700&display=swap" rel="stylesheet">
<style>
  :root{
    --navy:#1f2240;
    --navy-deep:#171a33;
    --red:#e8222a;
    --ink:#2b2b33;
    --muted:#7a7a82;
    --paper:#f2f2f2;
    --white:#ffffff;
  }
  *{box-sizing:border-box;margin:0;padding:0}
  html,body{width:1200px;height:2812px;overflow:hidden;background:var(--white)}
  body{font-family:"Poppins",sans-serif;color:var(--ink);position:relative}

  .site-header{height:148px;display:flex;align-items:center;justify-content:space-between;padding:0 80px;background:var(--white)}
  .brand{display:flex;align-items:center;gap:16px}
  .brand-dot{width:64px;height:64px;border-radius:50%;background:var(--red)}
  .brand-name{font-weight:700;font-size:24px;color:var(--navy);line-height:1.1;width:220px}
  .main-nav{display:flex;gap:60px;font-size:19px;font-weight:500}
  .main-nav a{color:var(--ink);text-decoration:none}
  .main-nav a.active{color:var(--red)}

  .hero{position:relative;height:612px;overflow:hidden}
  .hero-photo{position:absolute;inset:0;background:linear-gradient(90deg,#1c1f3a 0%,#3a3a52 40%,#9a8878 70%,#cdbba6 100%)}
  .hero-copy{position:absolute;left:80px;top:136px;color:var(--white)}
  .hero-title{font-size:66px;font-weight:700;line-height:1.1}
  .hero-sub{font-size:30px;line-height:1.35;margin-top:22px;width:520px}
  .btn{display:inline-flex;align-items:center;justify-content:center;font-weight:600;text-decoration:none;letter-spacing:.5px}
  .btn-red{background:var(--red);color:var(--white);width:468px;height:78px;font-size:30px;margin-top:36px}

  .qualify{background:var(--paper);height:780px;padding:56px 80px 0}
  .qualify-title{text-align:center;font-size:40px;font-weight:600;line-height:1.45;color:var(--ink)}
  .qualify-title span{display:block;color:var(--red)}
  .qualify-text{font-size:27px;line-height:56px;color:var(--muted);margin-top:36px}
  .qualify-sub{font-size:40px;font-weight:600;color:var(--red);margin-top:42px}
  .checklist{list-style:none;margin-top:10px}
  .checklist li{display:flex;align-items:center;gap:14px;font-size:28px;height:53px;color:var(--ink)}
  .checklist svg{width:30px;height:30px;flex:none}

  .benefits{display:flex;gap:4px;height:308px;background:var(--white)}
  .benefit{position:relative;flex:1;overflow:hidden}
  .benefit-photo{position:absolute;inset:0;background:linear-gradient(160deg,#5a5a66,#2a2c3e)}
  .benefit:nth-child(2) .benefit-photo{background:linear-gradient(160deg,#6c6660,#2e2e3a)}
  .benefit:nth-child(3) .benefit-photo{background:linear-gradient(160deg,#707078,#33354a)}
  .benefit-body{position:relative;display:flex;flex-direction:column;align-items:center;padding-top:44px;color:var(--white);text-align:center}
  .benefit-icon{width:104px;height:104px;border-radius:50%;background:var(--navy);display:flex;align-items:center;justify-content:center}
  .benefit:nth-child(2) .benefit-icon{background:#13b33b}
  .benefit-text{font-size:23px;line-height:1.35;margin-top:40px;width:360px}

  .apply{height:184px;background:var(--paper);display:flex;justify-content:center;padding-top:32px}
  .btn-navy{background:var(--navy);color:var(--white);width:376px;height:100px;font-size:32px}

  .action{background:var(--red);height:568px;text-align:center;color:var(--white);padding-top:92px}
  .action-title{font-size:52px;font-weight:700;letter-spacing:1px}
  .action-rule{width:84px;height:4px;background:var(--white);margin:14px auto 0}
  .action-text{font-size:26px;line-height:38px;width:900px;margin:34px auto 0}
  .btn-white{background:var(--white);color:var(--ink);width:400px;height:88px;font-size:30px;margin-top:30px}

  .site-footer{background:var(--navy-deep);height:212px;display:flex;align-items:center;justify-content:space-between;padding:0 80px;color:var(--white)}
  .site-footer .brand-name{color:var(--white)}
  .socials{display:flex;gap:26px;margin-left:60px}
  .socials span{width:22px;height:22px;border-radius:50%;background:var(--white)}
  .copyright{font-size:19px}
</style>
</head>
<body>

<header class="site-header">
  <div class="brand">
    <span class="brand-dot"></span>
    <span class="brand-name">Claimant Aid Pathway USA</span>
  </div>
  <nav class="main-nav">
    <a class="active" href="#">Home</a>
    <a href="#">About</a>
    <a href="#">Our Services</a>
    <a href="#">Contact</a>
  </nav>
</header>

<section class="hero">
  <div class="hero-photo" role="img" aria-label="Photo of a smiling senior couple looking at a tablet together"></div>
  <div class="hero-copy">
    <h1 class="hero-title">Social Security<br>Disability Benefits</h1>
    <p class="hero-sub">You may be eligible for as much as $1,700 per months!</p>
    <a class="btn btn-red" href="#">GET MY FREE EVALUATION</a>
  </div>
</section>

<section class="qualify">
  <h2 class="qualify-title">YOU MAY GET PAID FOR YOUR DISABILITY<span>KEEPING YOU OUT OF WORK!</span></h2>
  <p class="qualify-text">Lorem Ipsum is simply dummy the printing and typesetting industry. Lorem Ipsum is simply dummy the printing and typesetting industry.</p>
  <h3 class="qualify-sub">Do I qualify?</h3>
  <ul class="checklist">
    <li><svg viewBox="0 0 30 30"><rect x="2" y="2" width="26" height="26" rx="3" fill="none" stroke="#e8222a" stroke-width="3"/><path d="M8 15l5 5 10-11" fill="none" stroke="#e8222a" stroke-width="3.5"/></svg>Bullet points content here</li>
    <li><svg viewBox="0 0 30 30"><rect x="2" y="2" width="26" height="26" rx="3" fill="none" stroke="#e8222a" stroke-width="3"/><path d="M8 15l5 5 10-11" fill="none" stroke="#e8222a" stroke-width="3.5"/></svg>Bullet points content here</li>
    <li><svg viewBox="0 0 30 30"><rect x="2" y="2" width="26" height="26" rx="3" fill="none" stroke="#e8222a" stroke-width="3"/><path d="M8 15l5 5 10-11" fill="none" stroke="#e8222a" stroke-width="3.5"/></svg>Bullet points content here</li>
    <li><svg viewBox="0 0 30 30"><rect x="2" y="2" width="26" height="26" rx="3" fill="none" stroke="#e8222a" stroke-width="3"/><path d="M8 15l5 5 10-11" fill="none" stroke="#e8222a" stroke-width="3.5"/></svg>Bullet points content here</li>
    <li><svg viewBox="0 0 30 30"><rect x="2" y="2" width="26" height="26" rx="3" fill="none" stroke="#e8222a" stroke-width="3"/><path d="M8 15l5 5 10-11" fill="none" stroke="#e8222a" stroke-width="3.5"/></svg>Bullet points content here</li>
  </ul>
</section>

<section class="benefits">
  <div class="benefit">
    <div class="benefit-photo" role="img" aria-label="Photo of a person receiving documents at a desk"></div>
    <div class="benefit-body">
      <div class="benefit-icon"><svg width="54" height="54" viewBox="0 0 54 54"><circle cx="27" cy="27" r="22" fill="none" stroke="#fff" stroke-width="3"/><text x="27" y="37" text-anchor="middle" font-family="Poppins,sans-serif" font-size="28" font-weight="700" fill="#fff">$</text></svg></div>
      <p class="benefit-text">Receive the Compensation You Deserve!</p>
    </div>
  </div>
  <div class="benefit">
    <div class="benefit-photo" role="img" aria-label="Photo of a consultation meeting in an office"></div>
    <div class="benefit-body">
      <div class="benefit-icon"><svg width="54" height="54" viewBox="0 0 54 54"><path d="M8 10h38v26H24l-10 9v-9H8z" fill="none" stroke="#fff" stroke-width="3" stroke-linejoin="round"/></svg></div>
      <p class="benefit-text">FREE No Obligation Consultation Pay Nothing!</p>
    </div>
  </div>
  <div class="benefit">
    <div class="benefit-photo" role="img" aria-label="Photo of a team working together in an office"></div>
    <div class="benefit-body">
      <div class="benefit-icon"><svg width="54" height="54" viewBox="0 0 54 54"><rect x="12" y="24" width="30" height="22" rx="3" fill="none" stroke="#fff" stroke-width="3"/><path d="M18 24v-7a9 9 0 0 1 18 0v7" fill="none" stroke="#fff" stroke-width="3"/><circle cx="27" cy="35" r="3" fill="#fff"/></svg></div>
      <p class="benefit-text">Your Contact Information and Claim are Confidential!</p>
    </div>
  </div>
</section>

<section class="apply">
  <a class="btn btn-navy" href="#">APPLY NOW</a>
</section>

<section class="action">
  <h2 class="action-title">TAKE ACTION NOW</h2>
  <div class="action-rule"></div>
  <p class="action-text">Lorem Ipsum is simply dummy text of the printing and typesetting industry. Lorem Ipsum has been industry's standard dummy text ever since the 1500s, when an unknown printer</p>
  <a class="btn btn-white" href="#">CLAIM NOW ONLINE</a>
</section>

<footer class="site-footer">
  <div class="brand">
    <span class="brand-dot"></span>
    <span class="brand-name">Claimant Aid Pathway USA</span>
  </div>
  <div class="socials" aria-label="Social links">
    <span></span><span></span><span></span><span></span>
  </div>
  <p class="copyright">Copyright © 2019 All Rights</p>
</footer>

</body>
</html>
```